New residential property management company

I have a lot of name recognition in our smaller town due to owning a construction company here. I have now started a residential property management company representing landlords and tenants. Just trying to get my name out there and get some rentals to manage!

```html
<!DOCTYPE html>
<html lang="en">
<head>
<meta charset="utf-8">
<title>Calder Property Management – Postcard</title>
<link rel="stylesheet" href="https://fonts.googleapis.com/css2?family=Poppins:wght@400;500;600;700;800&display=swap">
<style>
:root{
  --blue-deep:#0a6fd0;
  --blue:#1f8fe0;
  --blue-light:#22aee6;
  --accent:#1fa8e6;
  --charcoal:#3f3f40;
  --ink:#222;
  --white:#fff;
  --bg-light:#b9b9b9;
  --bg-dark:#5f5f5f;
  --pool:#3c9ec0;
  --garden:#5a8a6a;
}
*{box-sizing:border-box;margin:0;padding:0}
html,body{width:1027px;height:1200px;overflow:hidden}
body{
  font-family:"Poppins",sans-serif;
  background:linear-gradient(135deg,var(--bg-light) 0%,#a5a5a5 50%,var(--bg-dark) 100%);
  position:relative;
}
.card{position:absolute;left:142px;width:753px;height:502px;background:var(--white);overflow:hidden}
.card--front{top:75px}
.card--back{top:649px}
.card__shapes{position:absolute;inset:0;width:100%;height:100%}
.abs{position:absolute}

.brand{display:flex;align-items:center;gap:10px;font-weight:600;letter-spacing:2px}
.brand__dot{border-radius:50%}
.brand--front{left:42px;top:48px;color:var(--white);font-size:46px}
.brand--front .brand__dot{width:48px;height:48px;background:var(--white)}
.brand--back{left:449px;top:52px;color:var(--ink);font-size:32px}
.brand--back .brand__dot{width:34px;height:34px;background:var(--ink)}

.headline{left:35px;top:150px;color:var(--white);font-weight:800;font-size:40px;line-height:1.1;letter-spacing:-.5px}
.subhead{left:35px;top:193px;color:var(--white);font-weight:700;font-size:21px;line-height:27px}
.rule{left:36px;top:254px;width:258px;height:1px;background:var(--white)}
.tagline{left:35px;top:261px;color:var(--white);font-size:17px;line-height:21px}

.portrait{left:34px;top:367px;width:122px;height:122px;border-radius:50%;background:#7d7d7d;display:flex;align-items:center;justify-content:center}
.portrait__photo{width:108px;height:108px;border-radius:50%;background:radial-gradient(circle at 50% 40%,#b89a86,#6d5646 70%,#2a2a2a)}
.person{left:179px;top:390px;color:var(--white)}
.person__name{font-size:24px;font-weight:700;line-height:1.2}
.person__role{font-size:11.5px;margin-top:4px}
.person__email{font-size:12px;margin-top:6px;display:flex;align-items:center;gap:6px}
.hl{color:var(--accent)}

.contact{left:525px;top:388px;color:var(--ink);font-size:12.5px;font-weight:600;line-height:18px}
.contact__row{display:flex;gap:7px;align-items:flex-start;margin-bottom:4px}
.icon{flex:none;width:18px;height:18px}
.phone-pill{left:526px;top:455px;width:183px;height:30px;border-radius:15px;background:linear-gradient(90deg,var(--blue-light),var(--blue-deep));color:var(--white);font-weight:700;font-size:20px;display:flex;align-items:center;justify-content:center;gap:10px}

.about{left:37px;top:32px;width:320px;color:var(--white)}
.about h2{font-size:22px;font-weight:500;line-height:1.2;margin-bottom:4px}
.about p{font-size:13.5px;font-weight:600;line-height:21px}
.about h2.services-title{margin-top:24px;margin-bottom:6px}
.services{list-style:none;font-size:13.5px;font-weight:600;line-height:16px}
.services li{position:relative;padding-left:18px;margin-bottom:9px}
.services li::before{content:"";position:absolute;left:0;top:6px;width:5px;height:5px;border-radius:50%;background:var(--white)}

.back-phone{left:50px;top:414px;color:var(--white);font-size:38px;font-weight:700;display:flex;align-items:center;gap:16px;line-height:1}
.back-web{left:50px;top:459px;color:var(--white);font-size:21px;display:flex;align-items:center;gap:10px}
.stamp{left:637px;top:32px;width:85px;height:85px;border:1px solid var(--ink)}
.address-line{left:467px;width:255px;height:1px;background:var(--ink)}
</style>
</head>
<body>

<section class="card card--front">
  <svg class="card__shapes" viewBox="0 0 753 502" aria-hidden="true">
    <defs>
      <linearGradient id="frontBlue" x1="0" y1="0" x2="1" y2="1">
        <stop offset="0" stop-color="#0a6fd0"/>
        <stop offset="1" stop-color="#22b4e8"/>
      </linearGradient>
      <linearGradient id="photoTone" x1="0" y1="0" x2="0" y2="1">
        <stop offset="0" stop-color="#9cc4e6"/>
        <stop offset=".45" stop-color="#c9bfae"/>
        <stop offset=".75" stop-color="#5a8a6a"/>
        <stop offset="1" stop-color="#3c9ec0"/>
      </linearGradient>
    </defs>
    <path d="M0 0 H466 L356 236 Q350 249 360 262 L434 356 H0 Z" fill="url(#frontBlue)"/>
    <g fill="none" stroke="#fff" stroke-opacity=".45" stroke-width=".8">
      <path d="M446 0 L335 236 Q329 249 339 262 L455 410 L420 502"/>
      <path d="M434 0 L323 236 Q317 249 327 262 L446 410 L410 502"/>
      <path d="M422 0 L311 236 Q305 249 315 262 L437 410 L400 502"/>
    </g>
    <path d="M0 356 H434 L482 411 L443 502 H0 Z" fill="#3f3f40"/>
    <path d="M497 0 H753 V375 H497 Q485 375 477 366 L380 262 Q370 249 378 236 L483 12 Q489 0 497 0 Z" fill="url(#photoTone)" role="img" aria-label="Photo of an apartment complex with a pool and garden"/>
  </svg>

  <div class="abs brand brand--front"><span class="brand__dot"></span>CALDER</div>

  <h1 class="abs headline">RESIDENTIAL</h1>
  <p class="abs subhead">PROPERTY MANAGEMENT<br>COMPANY</p>
  <div class="abs rule"></div>
  <p class="abs tagline">Representing Landlords<br>and Tenants.</p>

  <div class="abs portrait"><div class="portrait__photo" role="img" aria-label="Portrait of the owner"></div></div>
  <div class="abs person">
    <p class="person__name">Renata Calder</p>
    <p class="person__role">Calder Property Management LLC (Owner)</p>
    <p class="person__email">
      <svg class="icon" viewBox="0 0 18 18" style="width:15px;height:15px"><circle cx="9" cy="9" r="8" fill="none" stroke="#fff"/><rect x="5" y="6" width="8" height="6" fill="#1fa8e6"/><path d="M5 6 L9 9.5 L13 6" fill="none" stroke="#fff" stroke-width=".8"/></svg>
      <span><span class="hl">mrscalder</span>@mailbox.com</span>
    </p>
  </div>

  <div class="abs contact">
    <div class="contact__row">
      <svg class="icon" viewBox="0 0 18 18"><circle cx="9" cy="9" r="8" fill="none" stroke="#333"/><path d="M9 4 a3 3 0 0 1 3 3 c0 2-3 6-3 6 s-3-4-3-6 a3 3 0 0 1 3-3z" fill="#1fa8e6"/><circle cx="9" cy="7" r="1" fill="#fff"/></svg>
      <span>218 Birchwood Hollow<br>Road Millbrook, OR 97400</span>
    </div>
    <div class="contact__row">
      <svg class="icon" viewBox="0 0 18 18"><circle cx="9" cy="9" r="8" fill="none" stroke="#333"/><circle cx="9" cy="9" r="4.5" fill="none" stroke="#1fa8e6"/><path d="M4.5 9 H13.5 M9 4.5 V13.5" stroke="#1fa8e6" stroke-width=".8"/></svg>
      <span>www.<span class="hl">calderproperty</span>.com</span>
    </div>
  </div>
  <div class="abs phone-pill">
    <svg viewBox="0 0 16 16" width="13" height="13"><path d="M4 1 L6 5 L4.5 6.5 Q6 9.5 9.5 11.5 L11 10 L15 12 L13.5 15 Q6 14 1 3 Z" fill="#fff"/></svg>
    541.555.0182
  </div>
</section>

<section class="card card--back">
  <svg class="card__shapes" viewBox="0 0 753 502" aria-hidden="true">
    <defs>
      <linearGradient id="backBlue" x1="0" y1="0" x2="1" y2="1">
        <stop offset="0" stop-color="#1f8fe0"/>
        <stop offset="1" stop-color="#22b4e8"/>
      </linearGradient>
    </defs>
    <path d="M0 0 H449 L340 235 Q333 250 344 265 L452 392 H0 Z" fill="url(#backBlue)"/>
    <path d="M0 392 H452 L464 408 L425 502 H0 Z" fill="#3f3f40"/>
  </svg>

  <div class="abs about">
    <h2>About Us</h2>
    <p>We are excited to handle every aspect of managing your investment property. Single family, multi family, multi unit dwellings, and apartment complexes.</p>
    <h2 class="services-title">What We Do</h2>
    <ul class="services">
      <li>Take photo and post pictures<br>of listing</li>
      <li>Post daily content to engage<br>target market</li>
      <li>Reply to potential buyers and sellers<br>via social media</li>
      <li>Hashtag research</li>
      <li>Need something else? just ask!</li>
    </ul>
  </div>

  <div class="abs back-phone">
    <svg viewBox="0 0 16 16" width="22" height="22"><path d="M4 1 L6 5 L4.5 6.5 Q6 9.5 9.5 11.5 L11 10 L15 12 L13.5 15 Q6 14 1 3 Z" fill="none" stroke="#fff" stroke-width="1.4"/></svg>
    541.555.0182
  </div>
  <div class="abs back-web">
    <svg viewBox="0 0 18 18" width="27" height="27"><circle cx="9" cy="9" r="8" fill="none" stroke="#fff" stroke-width=".8"/><circle cx="9" cy="9" r="5" fill="none" stroke="#1fa8e6"/><path d="M4 9 H14 M9 4 V14" stroke="#1fa8e6" stroke-width=".8"/></svg>
    <span>www.<span class="hl">calderproperty</span>.com</span>
  </div>

  <div class="abs brand brand--back"><span class="brand__dot"></span>CALDER</div>
  <div class="abs stamp"></div>
  <div class="abs address-line" style="top:278px"></div>
  <div class="abs address-line" style="top:327px"></div>
  <div class="abs address-line" style="top:376px"></div>
</section>

</body>
</html>
```